US Based Startup requires Website Design for Velmora Cell

We are launching a battery technology called "Velmora Cell" for which we need an elegant website design. We use red and black to represent positive and negative node color used in battery. The background is white. The font must provide more wide space and easy to read.
Velmora CellTM is a technology that uses fast switches, such as transistor switches, to make batteries more efficient. The novel technology can be implemented in all types of batteries – including non-rechargeable batteries, rechargeable batteries, wet-cell batteries and all metal oxide batteries.
Normal batteries are “non-switching”, that is, these batteries can only be connected to one another in parallel or series connections. Parallel connections enable batteries to charge faster whilst series connections enable the battery to discharge more efficiently to the load.
Velmora CellTM technology enables batteries to be connected in a third connection method called “duo-braidTM” that combines the benefit of faster charging of the batteries with renewable energy source, such as solar, in parallel connection, and then quickly re-configures the same batteries using the fast transistor switches, to be connected in series with the load, to discharge efficiently.

Target Market(s)

Renewable energy

Industry/Entity Type

Renewable

Coding

Coded - Design and coding required

Number of Pages Required

5+ page

Requirements
Must have
• The primary colors are red and black for logo and fonts. The background is white.
The font must be easy to read type of fonts with more white space. Only pictures will be in full color.
Nice to have
• Elegant and simple design bringing out a new battery concept to the energy industry.

```html
<!DOCTYPE html>
<html lang="en">
<head>
<meta charset="utf-8">
<title>Velmora Cell</title>
<link href="https://fonts.googleapis.com/css2?family=Oswald:wght@400;500;600&family=Open+Sans:wght@400;600&display=swap" rel="stylesheet">
<style>
:root{
  --red:#e0061b;
  --black:#000;
  --ink:#222;
  --text:#333;
  --white:#fff;
  --mist:#e1e4e9;
  --grey:#c9c9c9;
}
*{margin:0;padding:0;box-sizing:border-box}
html,body{width:1200px;height:2816px;overflow:hidden;background:var(--white)}
body{position:relative;font-family:'Open Sans',sans-serif;color:var(--text)}
.abs{position:absolute}
.head-font{font-family:'Oswald',sans-serif}

.topline{position:absolute;left:0;top:0;width:1200px;height:8px;background:var(--red)}
.site-header{position:absolute;left:0;top:8px;width:1200px;height:106px;background:var(--white)}
.brand{position:absolute;display:flex;align-items:center;gap:10px;font-family:'Oswald',sans-serif;font-weight:600;text-transform:uppercase;letter-spacing:1px}
.brand-dot{width:34px;height:34px;border-radius:50%;background:var(--red)}
.site-header .brand{left:112px;top:30px;font-size:28px;color:var(--black)}
.main-nav{position:absolute;left:443px;top:38px;display:flex;gap:35px;font-family:'Oswald',sans-serif;font-weight:500;font-size:14px;color:var(--black);text-transform:uppercase}
.main-nav .active{color:var(--red)}
.login-btn{position:absolute;left:959px;top:27px;width:130px;height:41px;border-radius:21px;background:var(--red);color:var(--white);font-family:'Oswald',sans-serif;font-weight:500;font-size:15px;display:flex;align-items:center;justify-content:center;gap:6px;box-shadow:0 3px 8px rgba(0,0,0,.25)}

.hero{position:absolute;left:0;top:114px;width:1200px;height:600px;background:linear-gradient(180deg,#163040 0%,#4f6a73 35%,#9b8f7e 58%,#4c6a3a 78%,#23361c 100%)}
.hero-title{position:absolute;left:150px;top:146px;width:480px;font-family:'Oswald',sans-serif;font-weight:600;font-size:48px;line-height:65px;color:var(--white);text-transform:uppercase}
.hero-btn{position:absolute;left:150px;top:371px;width:172px;height:53px;border-radius:27px;background:var(--red);color:var(--white);font-family:'Oswald',sans-serif;font-weight:500;font-size:18px;display:flex;align-items:center;justify-content:center;text-transform:uppercase}
.hero-arrow{position:absolute;top:251px;width:53px;height:53px;border-radius:50%;background:rgba(255,255,255,.85);display:flex;align-items:center;justify-content:center}
.hero-arrow.prev{left:60px}
.hero-arrow.next{left:1081px}

.section-title{position:absolute;font-family:'Oswald',sans-serif;font-weight:600;font-size:38px;color:var(--black);text-transform:uppercase;white-space:nowrap}
.section-title span{color:var(--red)}
.title-rule{position:absolute;width:92px;height:3px;background:var(--red)}

.about-visual{position:absolute;left:112px;top:900px;width:453px;height:252px;border-radius:22px;background:linear-gradient(90deg,#e4e6f0 0%,#dfe2ee 22%,#4a8fdc 24%,#7db7ec 45%,#5d9c3a 75%,#3f7a2a 100%);box-shadow:0 14px 20px rgba(0,0,0,.15)}
.about-text{position:absolute;left:600px;top:920px;width:492px;font-size:15px;line-height:30px;color:var(--text)}

.focus{position:absolute;left:0;top:1301px;width:1200px;height:673px;background:var(--mist)}
.focus-card{position:absolute;width:471px;height:184px;border-radius:92px;background:var(--white);box-shadow:0 6px 14px rgba(0,0,0,.12)}
.focus-icon{position:absolute;top:21px;width:140px;height:140px;border-radius:50%;background:var(--red)}
.focus-card h3{position:absolute;top:24px;font-family:'Oswald',sans-serif;font-weight:500;font-size:18px;color:var(--red);text-transform:uppercase}
.focus-card p{position:absolute;top:64px;width:260px;font-size:15px;line-height:30px;color:var(--text)}
.focus-card.left .focus-icon{left:318px}
.focus-card.left h3{right:171px}
.focus-card.left p{right:171px;text-align:right}
.focus-card.right .focus-icon{left:13px}
.focus-card.right h3{left:170px}
.focus-card.right p{left:170px}

.review{position:absolute;top:2181px;width:356px;height:241px;background:var(--white);box-shadow:0 2px 12px rgba(0,0,0,.14)}
.review .quote{position:absolute;left:22px;top:10px;font-family:'Oswald',sans-serif;font-size:26px;color:var(--red)}
.review p{position:absolute;left:22px;top:48px;width:320px;font-size:15px;line-height:30px;color:#555}
.review .avatar{position:absolute;left:22px;top:165px;width:55px;height:55px;border-radius:50%;background:linear-gradient(135deg,#b9b4ae,#4b4a4a)}
.review .name{position:absolute;left:96px;top:178px;font-family:'Oswald',sans-serif;font-weight:500;font-size:18px;color:var(--red);text-transform:uppercase}

.site-footer{position:absolute;left:0;top:2514px;width:1200px;height:302px;background:var(--black);border-top:4px solid var(--red)}
.site-footer .brand{left:0;width:1200px;justify-content:center;top:56px;font-size:30px;color:var(--white)}
.site-footer .brand-dot{width:32px;height:32px}
.foot-nav{position:absolute;left:0;top:146px;width:1200px;display:flex;justify-content:center;gap:22px;font-family:'Oswald',sans-serif;font-size:16px;color:var(--white);text-transform:uppercase}
.socials{position:absolute;left:0;top:192px;width:1200px;display:flex;justify-content:center;gap:11px}
.socials span{width:32px;height:32px;border-radius:50%;background:var(--white)}
.socials span.yt{background:var(--red)}
.copyright{position:absolute;left:0;top:252px;width:1200px;text-align:center;font-family:'Oswald',sans-serif;font-size:15px;color:var(--white)}
.copyright em{font-style:normal;color:var(--red)}
</style>
</head>
<body>

<div class="topline"></div>
<header class="site-header">
  <div class="brand"><span class="brand-dot"></span>Velmora Cell</div>
  <nav class="main-nav">
    <span class="active">Home</span><span>About</span><span>Services</span><span>Indutries</span><span>Reviews</span><span>Contact Us</span>
  </nav>
  <div class="login-btn">
    <svg width="12" height="13" viewBox="0 0 12 13"><circle cx="6" cy="3.5" r="3" fill="#fff"/><path d="M0 13c0-4 2.5-6 6-6s6 2 6 6z" fill="#fff"/></svg>
    LOGIN
  </div>
</header>

<section class="hero" role="img" aria-label="Solar panels and wind turbines on grass beside white battery storage containers at sunset">
  <h1 class="hero-title">Lorem ipsum dolor sit amet, consectetur adipiscing elit.</h1>
  <div class="hero-btn">Get Started</div>
  <div class="hero-arrow prev"><svg width="14" height="20" viewBox="0 0 14 20"><path d="M10 3 3 10l7 7" fill="none" stroke="#e0061b" stroke-width="2.5"/></svg></div>
  <div class="hero-arrow next"><svg width="14" height="20" viewBox="0 0 14 20"><path d="M4 3l7 7-7 7" fill="none" stroke="#e0061b" stroke-width="2.5"/></svg></div>
</section>

<section class="about">
  <div class="about-visual" role="img" aria-label="Battery whose casing shows a tree and solar panels on a green field under blue sky"></div>
  <h2 class="section-title" style="left:600px;top:836px"><span>About</span> Velmora Cell</h2>
  <div class="title-rule" style="left:600px;top:898px"></div>
  <p class="about-text">Sed ut perspiciatis unde omnis iste natus error sit voluptatem accus antium doloremque laudantium, totam rem aperiam, eaque ipsa quae ab illo inventore veritatis et quasi architecto beatae vitae dicta sunt explicabo. Nemo enim ipsam voluptatem quia voluptas sit aspernatur aut odit aut fugit, sed quia consequuntur magni dolores eos qui ratione voluptatem sequi nesciunt. Neque porro quisquam est, qui dolorem ipsum quia dolor sit amet, consectetur, adipisci velit, sed quia non numquam eius modi tempora incidunt ut labore et dolore magnam aliquam quaerat voluptatem.</p>
</section>

<section class="focus">
  <h2 class="section-title" style="left:0;width:1200px;text-align:center;top:84px"><span>Our</span> Focus Area</h2>
  <div class="title-rule" style="left:554px;top:147px"></div>

  <div class="focus-card left" style="left:112px;top:185px">
    <h3>Thermal Energy</h3>
    <p>Sed ut perspiciatis unde omnis iste natus error sit voluptatem accusant ium doloremque lauda.</p>
    <div class="focus-icon" role="img" aria-label="Light bulb with leaf icon"></div>
  </div>
  <div class="focus-card right" style="left:610px;top:185px">
    <div class="focus-icon" role="img" aria-label="Wind turbine icon"></div>
    <h3>Wind Energy</h3>
    <p>Sed ut perspiciatis unde omnis iste natus error sit voluptatem accusant ium doloremque lauda.</p>
  </div>
  <div class="focus-card left" style="left:112px;top:396px">
    <h3>Solar Energy</h3>
    <p>Sed ut perspiciatis unde omnis iste natus error sit voluptatem accusant ium doloremque lauda.</p>
    <div class="focus-icon" role="img" aria-label="Solar panel with sun and battery icon"></div>
  </div>
  <div class="focus-card right" style="left:610px;top:396px">
    <div class="focus-icon" role="img" aria-label="Tidal turbine in waves icon"></div>
    <h3>Tidal Energy</h3>
    <p>Sed ut perspiciatis unde omnis iste natus error sit voluptatem accusant ium doloremque lauda.</p>
  </div>
</section>

<section class="reviews">
  <h2 class="section-title" style="left:0;width:1200px;text-align:center;top:2061px"><span>Our</span> Client Testimonials</h2>
  <div class="title-rule" style="left:554px;top:2124px"></div>

  <article class="review" style="left:55px">
    <span class="quote">&ldquo;</span>
    <p>Sed ut perspiciatis unde omnis iste natus error sit voluptatem accusantium dolor emque laudantium, totam rem aperiam, eaque ipsa quae ab illo inventore .</p>
    <div class="avatar" role="img" aria-label="Client portrait"></div>
    <span class="name">Mara Quill</span>
  </article>
  <article class="review" style="left:423px">
    <span class="quote">&ldquo;</span>
    <p>Sed ut perspiciatis unde omnis iste natus error sit voluptatem accusantium dolor emque laudantium, totam rem aperiam, eaque ipsa quae ab illo inventore .</p>
    <div class="avatar" role="img" aria-label="Client portrait"></div>
    <span class="name">Mara Quill</span>
  </article>
  <article class="review" style="left:790px">
    <span class="quote">&ldquo;</span>
    <p>Sed ut perspiciatis unde omnis iste natus error sit voluptatem accusantium dolor emque laudantium, totam rem aperiam, eaque ipsa quae ab illo inventore .</p>
    <div class="avatar" role="img" aria-label="Client portrait"></div>
    <span class="name">Mara Quill</span>
  </article>
</section>

<footer class="site-footer">
  <div class="brand"><span class="brand-dot"></span>Velmora Cell</div>
  <nav class="foot-nav">
    <span>Home</span><span>|</span><span>About</span><span>|</span><span>Services</span><span>|</span><span>Indutries</span><span>|</span><span>Reviews</span><span>|</span><span>Contact</span>
  </nav>
  <div class="socials"><span></span><span></span><span></span><span class="yt"></span></div>
  <p class="copyright">&copy; Copyrights 2021 <em>Velmora Cell</em> &nbsp;&nbsp;|&nbsp;&nbsp; All Rights Reserved</p>
</footer>

</body>
</html>
```